VORLEN Website Design

We need a website designed for our company VORLEN. We are a luxury lifestyle club that will provide benefits and services for our members. The site should be clean & sleek, preferably using black and white (or darker colors). (example sites: brimvale.example, tusko.example)

Here is a link of a sample page I did using wix. (https://pelmundry4.sitebuild.example/mypage) This can be used to get a general idea.

Target Market(s)

Upper Middle Class in the United States

Number of Pages Required

5+ page

Font styles to use
Sans Serif
Other font styles liked:
• Arial (or other similar fonts)

Requirements
Must have
• A clean design that is eye-catching and speaks to our company.
Nice to have
• Ideas for copy.

```html
<!DOCTYPE html>
<html lang="en">
<head>
<meta charset="utf-8">
<title>VORLEN — About</title>
<link href="https://fonts.googleapis.com/css2?family=Figtree:wght@300;400;700&display=swap" rel="stylesheet">
<style>
  :root {
    --ink: #0b0b0b;
    --header-bg: #141414;
    --panel-bg: rgba(8, 8, 8, 0.95);
    --footer-bg: #000000;
    --paper: #ffffff;
    --text-light: #ffffff;
    --button-bg: #f2f2f2;
    --button-text: #222222;
    --warm-dark: #3a1a0a;
    --warm-mid: #a5501f;
    --warm-light: #e79a5c;
  }
  * { box-sizing: border-box; margin: 0; padding: 0; }
  html, body {
    width: 1200px;
    height: 1198px;
    overflow: hidden;
    background: var(--paper);
    font-family: "Figtree", Arial, sans-serif;
    color: var(--text-light);
  }
  .page { position: relative; width: 1200px; height: 1198px; }

  .site-header {
    position: absolute; top: 0; left: 0;
    width: 1200px; height: 64px;
    background: var(--header-bg);
  }
  .brand {
    position: absolute; left: 236px; top: 14px;
    font-size: 28px; font-weight: 300; letter-spacing: 0.5px;
  }
  .main-nav {
    position: absolute; top: 24px; left: 502px;
    display: flex; gap: 33px;
    font-size: 12px; font-weight: 400; letter-spacing: 0.2px;
  }

  .hero-photo {
    position: absolute; top: 64px; left: 0;
    width: 1200px; height: 636px;
    background:
      radial-gradient(ellipse at 50% 30%, var(--warm-light) 0%, transparent 45%),
      linear-gradient(180deg, var(--warm-dark) 0%, var(--warm-mid) 35%, #7a3414 65%, var(--warm-dark) 100%);
  }

  .photo-frame {
    position: absolute; left: 163px; top: 352px;
    width: 571px; height: 507px;
    background: var(--paper);
    padding: 13px 0 11px;
    box-shadow: 0 4px 14px rgba(0,0,0,0.25);
  }
  .toast-photo {
    width: 100%; height: 100%;
    background: radial-gradient(ellipse at 45% 40%, #9a9a9a 0%, #3a3a3a 45%, #080808 85%);
  }

  .about-panel {
    position: absolute; left: 602px; top: 463px;
    width: 436px; height: 512px;
    background: var(--panel-bg);
    box-shadow: 0 6px 16px rgba(0,0,0,0.3);
  }
  .about-title {
    position: absolute; left: 61px; top: 46px;
    font-size: 28px; font-weight: 700; letter-spacing: 0.4px;
  }
  .about-tagline {
    position: absolute; left: 61px; top: 118px;
    font-size: 24px; font-weight: 400; line-height: 28px;
  }
  .about-copy {
    position: absolute; left: 63px; top: 214px; width: 345px;
    font-size: 12px; line-height: 14.5px;
  }
  .about-copy p { margin-bottom: 15.5px; }
  .apply-button {
    position: absolute; left: 60px; top: 431px;
    width: 146px; height: 35px;
    border-radius: 18px;
    background: var(--button-bg);
    color: var(--button-text);
    font-size: 12px; line-height: 35px; text-align: center;
  }

  .site-footer {
    position: absolute; left: 0; top: 1061px;
    width: 1200px; height: 137px;
    background: var(--footer-bg);
  }
  .social-links {
    position: absolute; left: 504px; top: 50px;
    display: flex; gap: 6px;
  }
  .social-links span {
    display: block; width: 22px; height: 22px;
    background: var(--paper); border-radius: 3px;
  }
  .copyright {
    position: absolute; left: 0; top: 100px; width: 1200px;
    text-align: center; font-size: 12px;
  }
</style>
</head>
<body>
<div class="page">
  <header class="site-header">
    <div class="brand">VORLEN</div>
    <nav class="main-nav">
      <span>HOME</span><span>ABOUT</span><span>SERVICES AND BENEFITS</span><span>APPLY</span><span>CONTACT US</span>
    </nav>
  </header>

  <div class="hero-photo" role="img" aria-label="Hands raising champagne glasses in a toast in a warmly lit bar"></div>

  <div class="photo-frame">
    <div class="toast-photo" role="img" aria-label="Black and white photo of two hands clinking wine glasses"></div>
  </div>

  <section class="about-panel">
    <h1 class="about-title">ABOUT VORLEN</h1>
    <h2 class="about-tagline">The ultimate full<br>service lifestyle club</h2>
    <div class="about-copy">
      <p>VORLEN was formed to bring the best services, experiences, and exclusive opportunities to our members.</p>
      <p>With everything from private member events to private jet travel, the perks of being a VORLEN member are unmatched.</p>
      <p>Professional athletes, artists, musicians, corporate professionals: Our members come from diverse backgrounds.</p>
      <p>Comprehensive services like 24/7 concierge, accountants, attorneys, private advisers, planners, investment advisors and more.</p>
    </div>
    <div class="apply-button">Apply</div>
  </section>

  <footer class="site-footer">
    <div class="social-links" aria-label="Social links">
      <span></span><span></span><span></span><span></span><span></span><span></span><span></span>
    </div>
    <div class="copyright">© 2018 VORLEN</div>
  </footer>
</div>
</body>
</html>
```